Fishing charter business in Sitka Alaska needs new business card design

I have had the same design for 10 plus years, ready for something different. I have attached a copy of my current card and my website link is www.bluecoveangling.net
I am looking for something that will catch my clients eye, although I rely on word of mouth for most of my business a a nice business card will help people remember who I am. My business is located in Sitka Alaska, there are probably 20-30 other charter businesses in Sitka. I like the way my current card is laid out, with the two tone black and grey. I can leave it up to the designers to come up with something else.
Target Market(s)
men, women, couples. Anyone who likes fishing
Industry/Entity Type
Tourism
Contact Information for Business Card
Dorrance's Charter Service
Tidewater Rockline Sportfishing
Colors
Designer to choose colors to be used in the design.
Requirements
Must have
- Gilbert Dorrance
- PO Box 4716
- Kelp Bay, AK 99820
- Compass Rose image
- 100 Ton USCG Licensed Captain
- gdorrance@wavelink.net
- 907-555-0142
- www.bluecoveangling.net
Nice to have
- ghost image of "boat helm"
Should not have
- be to complex

```html
<!DOCTYPE html>
<html lang="en">
<head>
<meta charset="utf-8">
<title>Dorrance's Charter Service – Business Cards</title>
<link rel="stylesheet" href="https://fonts.googleapis.com/css2?family=Cormorant+SC:wght@500&family=Tinos&display=swap">
<style>
  :root {
    --ink: #0d0d0d;
    --paper: #ffffff;
    --backdrop: #d4d4d6;
  }
  * { margin: 0; padding: 0; box-sizing: border-box; }
  html, body { width: 1200px; height: 848px; overflow: hidden; }
  body {
    background: var(--backdrop);
    position: relative;
    font-family: "Tinos", "Times New Roman", serif;
  }
  .card { position: absolute; overflow: hidden; }
  .company-name, .tagline { white-space: nowrap; }

  /* Landscape card */
  .card--landscape {
    left: 70px; top: 241px; width: 640px; height: 366px;
    background: var(--ink); color: var(--paper);
  }
  .card--landscape .artwork {
    position: absolute; left: 0; top: 0; width: 285px; height: 366px;
  }
  .card--landscape .identity,
  .card--landscape .company,
  .card--landscape .contact {
    position: absolute; right: 26px; text-align: right;
  }
  .card--landscape .identity { top: 42px; }
  .card--landscape .company { top: 190px; }
  .card--landscape .contact { top: 252px; }
  .card--landscape .company-name { font-size: 26px; }

  /* Portrait card */
  .card--portrait {
    left: 800px; top: 127px; width: 330px; height: 594px;
    background: linear-gradient(to bottom, var(--paper) 0 225px, var(--ink) 225px 100%);
    text-align: center;
  }
  .card--portrait .identity { position: absolute; top: 22px; width: 100%; color: var(--ink); }
  .card--portrait .artwork { position: absolute; left: 40px; top: 72px; width: 250px; height: 270px; }
  .card--portrait .company { position: absolute; top: 402px; width: 100%; color: var(--paper); }
  .card--portrait .contact { position: absolute; top: 468px; width: 100%; color: var(--paper); }
  .card--portrait .company-name { font-size: 24px; }
  .card--portrait .tagline { font-size: 11px; letter-spacing: 1.3px; }

  .name { font-size: 26px; line-height: 1.1; }
  .title { font-size: 13px; margin-top: 4px; }
  .company-name {
    font-family: "Cormorant SC", "Times New Roman", serif;
    font-weight: 500; line-height: 1; letter-spacing: 0.5px;
  }
  .tagline {
    font-family: "Cormorant SC", "Times New Roman", serif;
    font-weight: 500; font-size: 12px; letter-spacing: 1.6px; margin-top: 5px;
    text-transform: lowercase;
  }
  .contact p { font-size: 13.5px; line-height: 18.5px; }
</style>
</head>
<body>

  <section class="card card--landscape">
    <svg class="artwork" viewBox="0 0 285 366" role="img" aria-label="Illustration: captain in a fedora at a ship's helm over a compass rose">
      <defs>
        <linearGradient id="art-land" x1="0" y1="0" x2="0" y2="1">
          <stop offset="0" stop-color="#ffffff"/>
          <stop offset="0.45" stop-color="#cfcfcf"/>
          <stop offset="1" stop-color="#0d0d0d"/>
        </linearGradient>
      </defs>
      <rect width="285" height="366" fill="url(#art-land)"/>
    </svg>
    <div class="identity">
      <p class="name">Gilbert Dorrance</p>
      <p class="title">100 Ton USCG Licensed Captain</p>
    </div>
    <div class="company">
      <p class="company-name">Dorrance's Charter Service</p>
      <p class="tagline">Tidewater Rockline Sportfishing</p>
    </div>
    <div class="contact">
      <p>PO Box 4716</p>
      <p>Kelp Bay, AK 99820</p>
      <p>907-555-0142</p>
      <p>gdorrance@wavelink.net</p>
      <p>www.bluecoveangling.net</p>
    </div>
  </section>

  <section class="card card--portrait">
    <div class="identity">
      <p class="name">Gilbert Dorrance</p>
      <p class="title">100 Ton USCG Licensed Captain</p>
    </div>
    <svg class="artwork" viewBox="0 0 250 270" role="img" aria-label="Illustration: captain in a fedora at a ship's helm over a compass rose">
      <defs>
        <linearGradient id="art-port" x1="0" y1="0" x2="0" y2="1">
          <stop offset="0" stop-color="#ffffff"/>
          <stop offset="0.4" stop-color="#cfcfcf"/>
          <stop offset="1" stop-color="#0d0d0d"/>
        </linearGradient>
      </defs>
      <rect width="250" height="270" fill="url(#art-port)"/>
    </svg>
    <div class="company">
      <p class="company-name">Dorrance's Charter Service</p>
      <p class="tagline">Tidewater Rockline Sportfishing</p>
    </div>
    <div class="contact">
      <p>PO Box 4716</p>
      <p>Kelp Bay, AK 99820</p>
      <p>907-555-0142</p>
      <p>gdorrance@wavelink.net</p>
      <p>www.bluecoveangling.net</p>
    </div>
  </section>

</body>
</html>
```